SipLoop Business Cards

Hi designers!

Here's some background on our start-up and this project:

SipLoop is a website that will allow users to order alcohol from nearby liquor stores and have it delivered to their homes in minutes. We are really excited to work on creating the best online, alcohol purchasing experience for the users.

So why SipLoop? We like to think of ourselves as that great friend who will get alcohol for you because he happens to have a car. We help you drink in with your friends, family, or guests. Our site will target students and young professionals (of drinking age) who are comfortable buying things online or through apps. We don't see this service as a luxury, VIP, or niche service in the least; instead, we think of us as a relaxed, service-driven start-up that believes in simple design and transparent .

Now, we want a business card that incorporates our newly acquired logo design and some complimenting colors and fonts. Feel free to do it single or double sided, although I'm a sucker for double...

If you happen to have any questions, want to throw some ideas around, or just want some feedback- email me at marco@siploop.example.

Marco Tessin
Founder

Industry/Entity Type

Business

Requirements
Must have
• Name, Position, Email, Cell-phone

No address, no fax, no land-line.

```html
<!DOCTYPE html>
<html lang="en">
<head>
<meta charset="utf-8">
<title>SipLoop Business Cards</title>
<link rel="stylesheet" href="https://fonts.googleapis.com/css2?family=Poppins:wght@400;600;700&display=swap">
<style>
  :root {
    --magenta: #b0208f;
    --yellow: #f7c319;
    --ink: #231f20;
    --paper: #ffffff;
    --backdrop: #f2f2f2;
    --text-font: "Poppins", "Century Gothic", sans-serif;
  }
  * { box-sizing: border-box; margin: 0; padding: 0; }
  html, body {
    width: 1200px;
    height: 1000px;
    overflow: hidden;
    background: var(--backdrop);
    font-family: var(--text-font);
  }
  .card {
    position: absolute;
    width: 760px;
    height: 440px;
    background: var(--paper);
    overflow: hidden;
    box-shadow: 0 2px 10px rgba(0,0,0,0.12);
  }

  /* Front side */
  .card--front { left: 90px; top: 40px; }
  .front__wordmark {
    position: absolute;
    left: 28px;
    top: 10px;
    font-size: 150px;
    font-weight: 700;
    line-height: 1;
    letter-spacing: -3px;
    color: var(--ink);
  }
  .front__band {
    position: absolute;
    left: -40px;
    top: 208px;
    width: 860px;
    height: 52px;
    background: var(--magenta);
    transform: rotate(-4deg);
    display: flex;
    align-items: center;
    justify-content: center;
  }
  .front__tagline {
    color: var(--paper);
    font-size: 22px;
    font-weight: 700;
    letter-spacing: 5px;
    text-transform: uppercase;
  }
  .front__person {
    position: absolute;
    left: 0;
    right: 0;
    top: 296px;
    text-align: center;
  }
  .front__name {
    font-size: 26px;
    font-weight: 600;
    letter-spacing: 4px;
    color: var(--ink);
  }
  .front__role {
    margin-top: 2px;
    font-size: 15px;
    letter-spacing: 4px;
    color: var(--magenta);
    text-transform: uppercase;
  }
  .front__contact {
    position: absolute;
    left: 0;
    right: 0;
    top: 384px;
    text-align: center;
    font-size: 19px;
    letter-spacing: 1px;
    color: var(--ink);
  }
  .front__divider {
    color: var(--yellow);
    margin: 0 12px;
  }

  /* Back side */
  .card--back { left: 350px; top: 530px; }
  .back__rule {
    position: absolute;
    left: 0;
    width: 100%;
    height: 16px;
    background: var(--yellow);
  }
  .back__rule--top { top: 0; }
  .back__rule--bottom { bottom: 0; }
  .back__bottles {
    position: absolute;
    left: 0;
    top: 16px;
    width: 330px;
    height: 408px;
    background: var(--magenta);
  }
  .back__brand {
    position: absolute;
    left: 330px;
    right: 0;
    top: 110px;
    text-align: center;
  }
  .back__wordmark {
    font-size: 84px;
    font-weight: 700;
    line-height: 1.1;
    letter-spacing: -2px;
    color: var(--ink);
  }
  .back__url {
    margin-top: 40px;
    font-size: 22px;
    letter-spacing: 1px;
    color: var(--magenta);
  }
</style>
</head>
<body>

<section class="card card--front">
  <div class="front__wordmark">SipLoop</div>
  <div class="front__band">
    <span class="front__tagline">We bring the drinks to you!</span>
  </div>
  <div class="front__person">
    <div class="front__name">Marco Tessin</div>
    <div class="front__role">Founder</div>
  </div>
  <div class="front__contact">
    marco@siploop.example<span class="front__divider">|</span>555.010.2468<span class="front__divider">|</span>siploop.example
  </div>
</section>

<section class="card card--back">
  <div class="back__rule back__rule--top"></div>
  <div class="back__bottles" role="img" aria-label="Silhouettes of two white wine bottles and a dark beer bottle on a magenta panel"></div>
  <div class="back__brand">
    <div class="back__wordmark">SipLoop</div>
    <div class="back__url">siploop.example</div>
  </div>
  <div class="back__rule back__rule--bottom"></div>
</section>

</body>
</html>
```